luxuous inflatable bath tub package design

We are a dutch company selling mostly inflatable products. The product is a luxuous inflatable bath tub. The bath tub is for adults who have no space for a bath tub in the bath room or for use in the garden/balcony with hot weather.

The package contains the bath tub, manual pump and a gift set containing a bath bomb, inflatable pillow and 5 hygienecovers.

The colors of the bath tub and the brand logo are black/white (see added logo) The final design should communicate luxury, warmth and a wellness feeling/spa feeling.

We have made photo's with our own model for the listing presentation. THis can be viewed at https://www.kavelo.com/nl/nl/p/meridel-opblaasbaar-zitbad-voor-volwassenen-morvixplo-met-velvora-giftset-ruud-vank-methode-opvouwbaar-inklapbaar-spa-bad-morvix-plo-ijsbad-opblaasbad/7411000065217390/?bltgh=xRtpLm-ZKAfdqWenb48TsQ.3_21.17.ProductTitle

In the file attached you can find the main photo of the listing and a photo of the empty bath tub. We sell the product online, so although we would like the package to show a small photo of the product at least somewhere, it is not nessecary to make it big.

Target Market(s)

Adults with small bathrooms, adults who like to take ice baths, adults who like to enjoy bath time in garden.

Industry/Entity Type

Inflatable bath tubs

Colors

Designer to choose colors to be used in the design.

Requirements
Must have
• Description of contents: "1x Meridel zitbad 1x Opblaaspomp 1x Verlengbuis 1x Handleiding Velvora Giftset bestaande uit een Meridel bruisbal, opblaasbaar zitkussen en 5 hygiënehoezen"

```html
<!DOCTYPE html>
<html lang="nl">
<head>
<meta charset="utf-8">
<title>Meridel – Luxe Opblaasbaar Bad verpakking</title>
<link href="https://fonts.googleapis.com/css2?family=Bebas+Neue&family=Montserrat:wght@500;600&family=Nunito:wght@400;800&family=Oswald:wght@500&display=swap" rel="stylesheet">
<style>
:root{
  --bg:#cfcfcf;
  --black:#0d0d0d;
  --white:#ffffff;
  --icon-grey:#a9a9a9;
  --ink:#1b1b1b;
  --side-title:#8c8c8c;
  --side-sub:#d6d6d6;
  --side-note:#bdbdbd;
}
*{margin:0;padding:0;box-sizing:border-box}
html,body{width:1200px;height:2477px;overflow:hidden;background:var(--bg)}
.canvas{position:relative;width:1200px;height:2477px}

.pack-front{position:absolute;width:1127px;height:795px;overflow:hidden;background:linear-gradient(135deg,#fafafa,#e6e6e6);box-shadow:0 20px 40px rgba(0,0,0,.25)}
.pack-front--preview{left:200px;top:130px;transform:scale(.7453);transform-origin:0 0}
.pack-front--main{left:57px;top:1612px}
.pack-front svg.shapes{position:absolute;left:0;top:0}

.brand{position:absolute;left:0;top:0;width:280px;height:230px;display:flex;flex-direction:column;align-items:center;justify-content:center;gap:14px}
.brand-dot{width:70px;height:70px;border:7px solid var(--white);border-radius:50%}
.brand-name{font-family:"Montserrat",sans-serif;font-weight:500;font-size:44px;color:var(--white);letter-spacing:1px;white-space:nowrap}

.headline{position:absolute;left:345px;top:30px;font-family:"Bebas Neue",sans-serif;font-weight:400;font-size:104px;line-height:1;color:var(--black);white-space:nowrap;transform:scaleX(.86);transform-origin:0 0}
.subline{position:absolute;left:347px;top:128px;font-family:"Montserrat",sans-serif;font-weight:500;font-size:28px;letter-spacing:3.2px;color:var(--black);white-space:nowrap}
.tagline{position:absolute;left:302px;top:197px;font-family:"Oswald",sans-serif;font-weight:500;font-size:27px;color:var(--white);white-space:nowrap;transform:scaleX(.85);transform-origin:0 0}

.features{position:absolute;left:60px;top:278px;list-style:none}
.feature{display:flex;align-items:center;height:135px}
.feature-icon{width:114px;height:114px;flex:none}
.feature-text{margin-left:18px;font-family:"Nunito",sans-serif;font-size:30px;line-height:37px;color:var(--ink);white-space:nowrap}
.feature-text b{font-weight:800}

.guarantee{position:absolute;left:33px;top:722px;font-family:"Montserrat",sans-serif;font-weight:500;font-size:43px;color:var(--white);white-space:nowrap}
.guarantee b{font-weight:600}

.product-photo{position:absolute;left:693px;top:218px;width:464px;height:464px;border-radius:50%;background:radial-gradient(ellipse at 50% 30%,#f4f4f4 0 34%,#d9d9d9 35%,#2a2a2a 36% 100%)}

.pack-side{position:absolute;left:57px;top:1010px;width:1127px;height:230px;background:var(--black);box-shadow:0 20px 40px rgba(0,0,0,.25);display:flex;align-items:center;padding-left:40px}
.side-brand{display:flex;flex-direction:column;align-items:center;gap:10px;width:200px;flex:none}
.side-brand .brand-name{font-size:36px}
.side-brand .brand-dot{width:56px;height:56px;border-width:6px}
.side-title{margin-left:50px;width:820px}
.side-title .title{font-family:"Bebas Neue",sans-serif;font-size:80px;line-height:1;color:var(--side-title);white-space:nowrap}
.side-title .sub{margin-top:4px;font-family:"Montserrat",sans-serif;font-weight:500;font-size:22px;letter-spacing:3px;color:var(--side-sub);white-space:nowrap}
.side-title .contents{margin-top:12px;font-family:"Nunito",sans-serif;font-size:16px;line-height:21px;color:var(--side-note)}

.caption{position:absolute;left:0;width:1200px;top:2424px;text-align:center;font-family:"Nunito",sans-serif;font-weight:800;font-size:42px;line-height:1;color:var(--black)}
</style>
</head>
<body>
<main class="canvas">

  <section class="pack-front pack-front--preview">
    <svg class="shapes" width="1127" height="795" viewBox="0 0 1127 795">
      <defs>
        <linearGradient id="metal-a" x1="0" x2="1" y1="0" y2="0">
          <stop offset="0" stop-color="#9a9a9a"/><stop offset=".3" stop-color="#e9e9e9"/><stop offset=".6" stop-color="#bdbdbd"/><stop offset="1" stop-color="#f0f0f0"/>
        </linearGradient>
        <pattern id="scallop-a" width="28" height="28" patternUnits="userSpaceOnUse"><circle cx="14" cy="0" r="14" fill="#f2f2f2"/></pattern>
      </defs>
      <rect x="0" y="0" width="1127" height="190" fill="url(#metal-a)"/>
      <circle cx="120" cy="90" r="215" fill="#9c9c9c"/>
      <circle cx="110" cy="85" r="205" fill="var(--black)"/>
      <path d="M270 190 H720 L690 245 H270 Z" fill="var(--black)"/>
      <rect x="0" y="690" width="1127" height="105" fill="var(--black)"/>
      <rect x="0" y="690" width="1127" height="14" fill="url(#scallop-a)"/>
      <circle cx="925" cy="450" r="290" fill="var(--black)"/>
      <circle cx="925" cy="450" r="240" fill="var(--white)"/>
    </svg>
    <div class="product-photo" role="img" aria-label="Productfoto: vrouw ontspant in het zwarte opblaasbare zitbad"></div>
    <div class="brand"><span class="brand-dot"></span><span class="brand-name">MERIDEL</span></div>
    <h1 class="headline">LUXE OPBLAASBAAR BAD</h1>
    <p class="subline">OPVOUWBAAR EN OPVOUWBAAR SPABAD</p>
    <p class="tagline">CREËER JE EIGEN SPA, GEWOON THUIS</p>
    <ul class="features">
      <li class="feature"><svg class="feature-icon" viewBox="0 0 114 114"><circle cx="57" cy="57" r="57" fill="var(--icon-grey)"/><path d="M57 28c4 14 20 20 16 40a16 16 0 0 1-32 0c0-10 8-14 8-24 6 6 6 12 6 12 4-8 2-18 2-28z" fill="var(--white)"/></svg><p class="feature-text"><b>3-Laagse isolatie</b> voor<br>het behouden van warmte</p></li>
      <li class="feature"><svg class="feature-icon" viewBox="0 0 114 114"><circle cx="57" cy="57" r="57" fill="var(--icon-grey)"/><rect x="47" y="28" width="20" height="40" fill="var(--white)"/><rect x="44" y="70" width="26" height="18" rx="3" fill="var(--white)"/></svg><p class="feature-text">Opblaasbaar bad, geschikt<br>voor <b>ieder huishouden</b></p></li>
      <li class="feature"><svg class="feature-icon" viewBox="0 0 114 114"><circle cx="57" cy="57" r="57" fill="var(--icon-grey)"/><path d="M32 84c0-30 20-48 52-50-2 32-20 52-50 52z" fill="var(--white)"/></svg><p class="feature-text"><b>Geniet en ontspan</b> net als<br>in een echte spa</p></li>
    </ul>
    <p class="guarantee"><b>+30 DAGEN</b> BEDENKTIJD</p>
  </section>

  <section class="pack-side">
    <div class="side-brand"><span class="brand-dot"></span><span class="brand-name">MERIDEL</span></div>
    <div class="side-title">
      <p class="title">LUXE OPBLAASBAAR BAD</p>
      <p class="sub">OPVOUWBAAR EN OPVOUWBAAR SPABAD</p>
      <p class="contents">1x Meridel zitbad · 1x Opblaaspomp · 1x Verlengbuis · 1x Handleiding · Velvora Giftset bestaande uit een Meridel bruisbal, opblaasbaar zitkussen en 5 hygiënehoezen</p>
    </div>
  </section>

  <section class="pack-front pack-front--main">
    <svg class="shapes" width="1127" height="795" viewBox="0 0 1127 795">
      <defs>
        <linearGradient id="metal-b" x1="0" x2="1" y1="0" y2="0">
          <stop offset="0" stop-color="#9a9a9a"/><stop offset=".3" stop-color="#e9e9e9"/><stop offset=".6" stop-color="#bdbdbd"/><stop offset="1" stop-color="#f0f0f0"/>
        </linearGradient>
        <pattern id="scallop-b" width="28" height="28" patternUnits="userSpaceOnUse"><circle cx="14" cy="0" r="14" fill="#f2f2f2"/></pattern>
      </defs>
      <rect x="0" y="0" width="1127" height="190" fill="url(#metal-b)"/>
      <circle cx="120" cy="90" r="215" fill="#9c9c9c"/>
      <circle cx="110" cy="85" r="205" fill="var(--black)"/>
      <path d="M270 190 H720 L690 245 H270 Z" fill="var(--black)"/>
      <rect x="0" y="690" width="1127" height="105" fill="var(--black)"/>
      <rect x="0" y="690" width="1127" height="14" fill="url(#scallop-b)"/>
      <circle cx="925" cy="450" r="290" fill="var(--black)"/>
      <circle cx="925" cy="450" r="240" fill="var(--white)"/>
    </svg>
    <div class="product-photo" role="img" aria-label="Productfoto: vrouw ontspant in het zwarte opblaasbare zitbad"></div>
    <div class="brand"><span class="brand-dot"></span><span class="brand-name">MERIDEL</span></div>
    <h2 class="headline">LUXE OPBLAASBAAR BAD</h2>
    <p class="subline">OPVOUWBAAR EN OPVOUWBAAR SPABAD</p>
    <p class="tagline">CREËER JE EIGEN SPA, GEWOON THUIS</p>
    <ul class="features">
      <li class="feature"><svg class="feature-icon" viewBox="0 0 114 114"><circle cx="57" cy="57" r="57" fill="var(--icon-grey)"/><path d="M57 28c4 14 20 20 16 40a16 16 0 0 1-32 0c0-10 8-14 8-24 6 6 6 12 6 12 4-8 2-18 2-28z" fill="var(--white)"/></svg><p class="feature-text"><b>3-Laagse isolatie</b> voor<br>het behouden van warmte</p></li>
      <li class="feature"><svg class="feature-icon" viewBox="0 0 114 114"><circle cx="57" cy="57" r="57" fill="var(--icon-grey)"/><rect x="47" y="28" width="20" height="40" fill="var(--white)"/><rect x="44" y="70" width="26" height="18" rx="3" fill="var(--white)"/></svg><p class="feature-text">Opblaasbaar bad, geschikt<br>voor <b>ieder huishouden</b></p></li>
      <li class="feature"><svg class="feature-icon" viewBox="0 0 114 114"><circle cx="57" cy="57" r="57" fill="var(--icon-grey)"/><path d="M32 84c0-30 20-48 52-50-2 32-20 52-50 52z" fill="var(--white)"/></svg><p class="feature-text"><b>Geniet en ontspan</b> net als<br>in een echte spa</p></li>
    </ul>
    <p class="guarantee"><b>+30 DAGEN</b> BEDENKTIJD</p>
  </section>

  <p class="caption">Packaging Front</p>
</main>
</body>
</html>
```